Redesign of Real Estate Agency Website

We need a redesign for our real estate agency website. Please see attached creative brief.

Target Market(s)

Refer to creative brief.

Industry/Entity Type

Real Estate

Requirements
Must have
• Refer to creative brief.

```html
<!DOCTYPE html>
<html lang="en">
<head>
<meta charset="utf-8">
<title>Islandkey Real Estate – Phuket Property</title>
<link rel="stylesheet" href="https://fonts.googleapis.com/css2?family=Arimo:wght@400;700&display=swap">
<style>
:root{
  --page:#f3f3f3;
  --panel:#ffffff;
  --line:#d6d6d6;
  --nav-top:#4a6fb3;
  --nav-bot:#13307a;
  --nav-active:#5d8ad6;
  --orange:#f5a31c;
  --orange-dark:#e08a00;
  --blue:#2aa3df;
  --red:#e4262a;
  --ink:#1d1d1d;
  --band:#e9e9e9;
}
*{box-sizing:border-box;margin:0;padding:0}
html,body{width:899px;height:1200px;overflow:hidden}
body{background:var(--page);font-family:"Arimo",Arial,sans-serif;color:var(--ink);position:relative}
.abs{position:absolute}

.brand{left:76px;top:14px;font-size:28px;color:#234a9a;letter-spacing:-0.5px}
.brand-sq{display:inline-block;width:10px;height:10px;background:#234a9a;margin-left:5px;vertical-align:middle}
.tagline{left:76px;top:49px;font-size:12px;color:#9a9a9a}

.main-nav{left:76px;top:65px;width:754px;height:21px;border-radius:4px;background:linear-gradient(var(--nav-top),var(--nav-bot));display:flex;padding-left:27px}
.main-nav a{color:#fff;text-decoration:none;font-size:11px;line-height:21px;padding:0 9px;margin-right:9px}
.main-nav a.active{background:linear-gradient(#7aa5e8,var(--nav-active))}

.hero-panel{left:76px;top:88px;width:754px;height:367px;background:var(--panel);border:1px solid var(--line)}
.hero{left:83px;top:96px;width:544px;height:353px;border-radius:3px;background:linear-gradient(180deg,#c9b3cf 0%,#e8c7b6 40%,#8b8f8c 62%,#a07a5e 82%,#6b4a34 100%)}
.dots{left:551px;top:431px;display:flex;gap:4px}
.dots i{width:10px;height:10px;border-radius:50%;background:#7a4b2a}
.dots i:first-child{background:var(--orange-dark)}

.side-head{left:634px;width:192px;height:21px;background:linear-gradient(#f7b43b,var(--orange));color:#fff;font-size:12px;line-height:21px;padding-left:8px}
.search-box{left:638px;top:119px;width:179px;height:138px;background:#fff;border:1px solid #e2e2e2;border-radius:3px}
.select{left:648px;width:159px;height:12px;border:1px solid #a9a9a9;border-radius:2px;background:linear-gradient(#fff,#ececec);font-size:8px;line-height:11px;padding-left:4px}
.select::after{content:"";position:absolute;right:0;top:0;width:10px;height:10px;background:#3b6fd0;border-radius:2px}
.search-btn{left:672px;top:228px;width:82px;height:13px;border-radius:3px;background:linear-gradient(#fbb44a,#f08a12);color:#fff;font-size:8px;font-weight:700;text-align:center;line-height:13px}
.adv{left:687px;top:245px;font-size:7px;color:#2233cc;text-decoration:underline}
.map-box{left:640px;top:290px;width:178px;height:156px;background:#fff;border:1px solid #e2e2e2;border-radius:3px}
.radio{left:654px;font-size:10px;color:#555}
.radio::before{content:"";display:inline-block;width:9px;height:9px;border-radius:50%;border:1px solid #999;margin-right:5px;vertical-align:-1px}
.radio.on::before{background:radial-gradient(#2a5ac8 40%,#fff 45%)}
.map{left:704px;top:300px;width:82px;height:134px;background:linear-gradient(#cfe6f5,#a8d0ec);border-radius:30px 10px 20px 40px}
.map-link{left:733px;top:437px;font-size:6px;color:#2233cc;text-decoration:underline}

.tab-band{left:76px;top:455px;width:754px;height:60px;background:var(--band)}
.tab{top:463px;height:52px;border-radius:6px 6px 0 0;font-size:18px;color:var(--blue);text-align:center}
.tab-sale{left:193px;width:259px;background:#fff;border:1px solid var(--line);border-bottom:none;line-height:54px}
.tab-rent{left:452px;width:257px;background:linear-gradient(#f9f9f9,#dcdcdc);border:1px solid #cfcfcf;line-height:60px}

.cats{left:76px;top:515px;width:754px;height:133px;background:#fff;border-left:1px solid var(--line);border-right:1px solid var(--line);border-bottom:1px solid var(--line)}
.thumb{top:540px;width:130px;height:80px}
.cat-label{top:629px;font-size:10px;color:var(--blue)}
.cat-label.hot{color:var(--red)}

.intro{left:76px;top:648px;width:754px;height:215px;background:#fff;border:1px solid var(--line);border-top:none}
.col{top:667px;font-size:9.4px;line-height:12.7px}
.col h2{font-weight:400;font-size:19px;color:var(--red);margin-bottom:6px}
.col h3{font-weight:400;font-size:9.4px;color:var(--blue)}
.col ul{list-style:none}
.col li{padding-left:8px;text-indent:-8px}
.col li::before{content:"• "}

.promo{top:872px;height:94px;background:linear-gradient(#fafafa,#e6e6e6);border:1px solid var(--line)}
.deals-title{left:78px;top:881px;font-size:22px;color:var(--blue);line-height:1}
.deals-big{left:82px;top:905px;font-size:34px;color:var(--blue);line-height:1}
.deals-sub{left:80px;top:943px;font-size:12px;color:#333}
.deals-img{left:231px;top:878px;width:137px;height:85px;background:linear-gradient(#c88a8f,#a2cde4 60%,#3f9ac4)}
.team-img{left:490px;top:888px;width:144px;height:77px;background:linear-gradient(#d9d9d9,#2a2a2a 60%);border-radius:30px 30px 0 0}
.team-text{left:376px;top:875px;font-size:13px;color:var(--blue);line-height:17px;z-index:2}
.news-title{left:654px;top:877px;font-size:14px;color:var(--blue)}
.news-text{left:654px;top:894px;font-size:11px;line-height:14px;color:#222}
.news-input{left:656px;top:942px;width:110px;height:16px;background:#fff;border:1px solid #888}
.news-btn{left:770px;top:943px;width:58px;height:14px;border-radius:7px;background:linear-gradient(#fbc55a,#e8a020);font-size:8px;text-align:center;line-height:14px;color:#222}

.footer{left:76px;top:978px;width:754px;height:222px;background:#f7f7f7;border:1px solid var(--line)}
.fcol{top:990px;font-size:6.4px;line-height:8.2px;color:#8a8a8a}
.fcol h4{font-weight:400;font-size:6.4px;margin-bottom:9px}
.fcol ul{list-style:none}
.fcol li{padding-left:8px}
.fcol li::before{content:"* "}
.fcol li.sub{padding-left:20px}
.fcol li.sub::before{content:"o "}
.badge{left:767px;top:980px;width:55px;height:207px}
.copy{left:76px;top:1156px;width:754px;text-align:center;font-size:6.5px;color:#888}
</style>
</head>
<body>

<div class="abs brand">Islandkey<span class="brand-sq"></span></div>
<div class="abs tagline">Phuket Property and Real</div>

<nav class="abs main-nav">
  <a href="#">Home</a><a href="#" class="active">Property for Sale</a><a href="#">Property for Rent</a><a href="#">Contact Us</a><a href="#">About Us</a><a href="#">List Your Property</a><a href="#">Property Buyer's Guide</a>
</nav>

<div class="abs hero-panel"></div>
<div class="abs hero" role="img" aria-label="Rooftop terrace with plunge pool and daybed overlooking the bay at dusk"></div>
<div class="abs dots"><i></i><i></i><i></i><i></i><i></i></div>

<div class="abs side-head" style="top:96px">Quick Property Search</div>
<div class="abs search-box"></div>
<div class="abs select" style="top:123px">Buy Property</div>
<div class="abs select" style="top:140px">Property Type</div>
<div class="abs select" style="top:157px">Region</div>
<div class="abs select" style="top:174px">District</div>
<div class="abs select" style="top:191px">Minimum Bedrooms</div>
<div class="abs select" style="top:208px">Maximum Price (THB)</div>
<div class="abs search-btn">Search</div>
<div class="abs adv">Advanced search</div>

<div class="abs side-head" style="top:264px">Search by Map</div>
<div class="abs map-box"></div>
<div class="abs radio on" style="top:304px">Buy</div>
<div class="abs radio" style="top:324px">Rent</div>
<div class="abs map" role="img" aria-label="Map of Phuket island divided into regions"></div>
<div class="abs map-link">View large map</div>

<div class="abs tab-band"></div>
<div class="abs tab tab-sale">Property for Sale</div>
<div class="abs tab tab-rent">Property for Rent</div>

<div class="abs cats"></div>
<div class="abs thumb" style="left:103px;background:linear-gradient(#c7d3db,#6d4a33)" role="img" aria-label="Thai style villa at dusk"></div>
<div class="abs thumb" style="left:247px;background:linear-gradient(#f2f2f2 40%,#58b7d8)" role="img" aria-label="Apartment living room with sea view pool"></div>
<div class="abs thumb" style="left:400px;background:linear-gradient(#d3a27a,#4d3b5b 50%,#e6d2c0)" role="img" aria-label="Featured property interior"></div>
<div class="abs thumb" style="left:542px;background:linear-gradient(#d3a27a,#4d3b5b 50%,#e6d2c0)" role="img" aria-label="Hot villa interior"></div>
<div class="abs thumb" style="left:686px;background:linear-gradient(#d3a27a,#4d3b5b 50%,#e6d2c0)" role="img" aria-label="Hot apartment interior"></div>
<div class="abs cat-label" style="left:99px;top:626px">Villas &amp; Houses for Sale</div>
<div class="abs cat-label" style="left:245px">Apartments &amp; Condos for Sale</div>
<div class="abs cat-label" style="left:398px">Property of the Month</div>
<div class="abs cat-label hot" style="left:540px">Hot Villas for Sale</div>
<div class="abs cat-label hot" style="left:684px">Hot Apartments for Sale</div>

<div class="abs intro"></div>
<section class="abs col" style="left:89px;width:380px">
  <h2>Welcome to Islandkey Real Estate</h2>
  <h3>The Services We Offer</h3>
  <p>Comprehensive service with integrity:</p>
  <ul>
    <li>Extensive selection of Phuket properties for sale and rent.</li>
    <li>Research and suggest properties that meet our clients' requirements.</li>
    <li>Arrange property sales and rentals viewings.</li>
    <li>Chauffer and escort clients throughout their property viewings.</li>
    <li>Provide independent advice regarding buying and renting property in Phuket.</li>
    <li>Offer unbiased legal information and can assist in appointing independent lawyers.</li>
    <li>Provide the best possible deal for our clients by negotiating with sellers and developers.</li>
    <li>Provide a comprehensive after-sales service by liaising with all parties involved.</li>
    <li>Provide regular updates to clients on their property purchase.</li>
    <li>Provide advice and support on all aspects of living in Phuket and Thailand.</li>
  </ul>
</section>
<section class="abs col" style="left:482px;width:335px">
  <h2>Why Use Islandkey Real Estate?</h2>
  <h3>Experience:</h3>
  <ul>
    <li>Islandkey Real Estate is one of the most experienced independent Real Estate agents focusing completely on Phuket.</li>
    <li>Our team has lived on Phuket for a total of over 90 years and our experience with Real Estate exceeds 30 years, so we feel we are very well qualified to provide high quality services to our clients.</li>
    <li>Proven track record with many satisfied clients.</li>
  </ul>
  <h3 style="margin-top:12px">Choice:</h3>
  <ul>
    <li>We have a wide selection of properties for sale and rent, including new developments, private homes, exclusive luxury homes and budget properties.</li>
    <li>We actively liaise with developers and sellers to ensure that our clients get the best deals and latest information.</li>
  </ul>
</section>

<div class="abs promo" style="left:76px;width:295px"></div>
<div class="abs promo" style="left:370px;width:266px"></div>
<div class="abs promo" style="left:635px;width:195px"></div>
<div class="abs deals-title">Check out our</div>
<div class="abs deals-big">hot deals</div>
<div class="abs deals-sub">on selected holiday rentals</div>
<div class="abs deals-img" role="img" aria-label="Resort pool at sunset"></div>
<div class="abs team-img" role="img" aria-label="Agency team standing together in black uniforms"></div>
<div class="abs team-text">We look forward to<br>hearing from you!</div>
<div class="abs news-title">Get Our Newsletter</div>
<div class="abs news-text">Get the latest Phuket<br>Real Estate news and deals<br>every month</div>
<div class="abs news-input"></div>
<div class="abs news-btn">SUBMIT</div>

<footer class="abs footer"></footer>
<div class="abs fcol" style="left:95px">
  <h4>phuket real estate for sale</h4>
  <ul>
    <li>phuket property for sale index</li><li>search property for sale in phuket</li><li>apartments &amp; condos for sale in phuket</li><li>villas &amp; houses for sale in phuket</li><li>land for sale in phuket</li><li>commercial property for sale in phuket</li><li>luxury property for sale</li><li>property for sale map</li><li>property buyer's guide for phuket</li>
    <li class="sub">why phuket?</li><li class="sub">property ownership rights</li><li class="sub">property taxes &amp; fees</li><li class="sub">land titles</li><li class="sub">land units</li><li class="sub">property faq</li>
  </ul>
</div>
<div class="abs fcol" style="left:278px">
  <h4>phuket property for rent</h4>
  <ul>
    <li>phuket property for rent index</li><li>search property for rent in phuket</li><li>phuket holiday rentals</li>
    <li class="sub">holiday villas</li><li class="sub">luxury villas</li><li class="sub">cheap villas</li><li class="sub">holiday apartments</li><li class="sub">holiday rentals booking guide</li><li class="sub">holiday rentals faq</li><li class="sub">terms &amp; conditions</li>
    <li>samui holiday rentals</li><li>phuket long-term rentals</li>
    <li class="sub">long-term villas &amp; houses</li><li class="sub">long-term apartments</li>
    <li>property for rent map</li>
  </ul>
</div>
<div class="abs fcol" style="left:464px">
  <h4>site links</h4>
  <ul><li>islandkey real estate index</li><li>privacy policy</li><li>disclaimer</li><li>site map</li></ul>
  <h4 style="margin-top:6px">about islandkey real estate</h4>
  <ul><li>about us</li><li>contact us</li><li>list your property</li><li class="sub">selling your property</li></ul>
</div>
<div class="abs fcol" style="left:620px">
  <h4>phuket info</h4>
  <ul><li>islandkey homepage</li><li>travel info</li><li>tours</li><li>dining &amp; nightlife</li><li>expats</li><li>directory</li><li>classified ads</li><li>hotels</li></ul>
</div>
<svg class="abs badge" viewBox="0 0 55 207" role="img" aria-label="Industry award ribbon">
  <rect width="55" height="5" fill="#c4161c"/>
  <path d="M0 5H55V207L27.5 185L0 207Z" fill="#111"/>
</svg>
<div class="abs copy">Phuket Real Estate from Islandkey | Copyright © Islandkey 2008. All Rights Reserved</div>

</body>
</html>
```